Relaunch Instagram Posts Design

We want to give you a better understanding about the expected outcome of this task, and give you a little bit of a background that should help you throughout.
We already have social media accounts, they aren’t active and the posts are outdated. We just finished our rebranding exercise, and accordingly we are planning to have a re-launch where we communicate our new identity, and rebuild our online existence, to enhance our social media presence and engagement.
Thus, we want to formulate the style of posting from the beginning, so that it reflects the identity overall and we can move forward with in a consistent manner.

Find attached details. We will share other files later. You need to read the attachment in the project to understand the requirement. Also, you should use the attached images in the project. You should also use products images from our website...www.bloomvelara.com
Our Primary color is #5725A9, PURPLE (based on color HEX Code)
Our Secondary colors #7C50BE, #A17BD3, #C5A6E8, #EAD1FD
Also, this secondary colors can be used #2B9348, #55A630, #80B918, #AACC00

Target Market(s)

Gift-givers who would like to bring a gift of value and meaning, representing the occasion

Industry/Entity Type

Flowers

Colors

Designer to choose colors to be used in the design.

Requirements
Must have
• Image based posts with little graphics + typography-based posts.... hammer on the emotional aspect, focusing on special moments such as using images related nice moments
Nice to have
• A full overview as in the brief (with all 21 posts), to give the sense of the design direction for us to know if it fits our new brand vision or not.
Should not have
• A typical commercial design direction that focuses so much on direct product communication. This definitely will be there, but we want this to be integrated with the other aspects.

```html
<!DOCTYPE html>
<html lang="en">
<head>
<meta charset="utf-8">
<title>Captured in a Dance of Droplets</title>
<link rel="stylesheet" href="https://fonts.googleapis.com/css2?family=Caveat:wght@500;700&family=Crimson+Text&display=swap">
<style>
  :root {
    --frame-purple: #5d2fb0;
    --stroke-purple: #6a45b8;
    --serif-purple: #8a57c9;
    --ink-dark: #4a4244;
    --ink-rose: #b57b6f;
    --panel-top: #ffffff;
    --panel-bottom: #fcf2f3;
    --photo-grey: #9b9597;
    --photo-rose: #b0182c;
    --bloom-coral: #f26a70;
    --bloom-peach: #f9b59a;
  }
  * { margin: 0; padding: 0; box-sizing: border-box; }
  html, body { width: 1200px; height: 1200px; overflow: hidden; background: #fff; }
  .post {
    position: relative;
    width: 1200px;
    height: 1200px;
    overflow: hidden;
    background: linear-gradient(180deg, var(--panel-top) 0%, var(--panel-bottom) 100%);
  }
  .rose-photo {
    position: absolute;
    left: 647px; top: 0;
    width: 553px; height: 1200px;
    background: linear-gradient(180deg, #a19b9d 0%, var(--photo-grey) 45%, #8f3b48 60%, var(--photo-rose) 75%, #8e1024 100%);
  }
  .bloom-illustration {
    position: absolute;
    left: 0; top: 0;
    width: 640px; height: 640px;
    background: radial-gradient(circle at 0 0,
      var(--bloom-coral) 0%,
      var(--bloom-peach) 35%,
      rgba(249, 181, 154, 0) 68%);
  }
  .frame {
    position: absolute;
    left: 37px; top: 37px;
    width: 1126px; height: 1126px;
    border: 4px solid var(--frame-purple);
  }
  .headline { position: absolute; left: 0; top: 0; width: 1200px; height: 1200px; }
  .script { font-family: "Caveat", cursive; font-weight: 500; }
  .script-dark { fill: var(--ink-dark); }
  .script-rose { fill: var(--ink-rose); }
  .tagline { font-family: "Crimson Text", serif; fill: var(--serif-purple); font-size: 49px; }
  .brush-stroke { fill: var(--stroke-purple); }
</style>
</head>
<body>
  <main class="post">
    <div class="rose-photo" role="img" aria-label="Close-up photograph of a red rose with water droplets falling onto its petals against a grey background"></div>
    <div class="bloom-illustration" role="img" aria-label="Illustrated coral-pink gerbera flower with green leaves in the top-left corner"></div>
    <div class="frame"></div>

    <svg class="headline" viewBox="0 0 1200 1200" xmlns="http://www.w3.org/2000/svg">
      <text class="script script-dark" x="100" y="561" font-size="160">Captured</text>
      <text class="script script-dark" x="476" y="612" font-size="74" text-anchor="end">in a</text>
      <text class="script script-rose" x="128" y="694" font-size="190">Dance</text>
      <text class="script script-dark" x="570" y="755" font-size="68" text-anchor="end">of droplets,</text>
      <path class="brush-stroke" d="M112 806 Q350 794 596 790 Q350 802 120 822 Q106 822 106 814 Z"/>
      <text class="tagline" x="580" y="864" text-anchor="end">The rose’s elegance</text>
      <text class="tagline" x="580" y="922" text-anchor="end">is unfading</text>
    </svg>
  </main>
</body>
</html>
```